I need podcast cover art that could also be incorporated into a website and social media accounts. I originally planned on calling the podcast "Mendral Access Lab" but need to change it to "Mendral Access Roundtable," and its purpose is to educate and inspire people on how we can deliver more affordable, higher quality health care in the United States. The target audience is anyone working in a healthcare related industry (doctors, nurses, healthcare insurers, policymakers involved in writing healthcare policy, etc...). The program will be well-researched and the tone will be upbeat. I will be interviewing experts in healthcare delivery including innovators who have come up with creative solutions to improving healthcare quality where they work. I want to keep the design very clean, simple, and modern looking. Thank you so much - I am looking forward to seeing your designs!

Target Market(s)

working professionals and students in healthcare-related fields

Industry/Entity Type

Health Care

Font styles to use
Sans Serif

Colors

Designer to choose colors to be used in the design.

Requirements
Must have
• very clean, simple and modern looking

```html
<!DOCTYPE html>
<html lang="en">
<head>
<meta charset="utf-8">
<title>Mendral Access Roundtable – Podcast Cover</title>
<link rel="stylesheet" href="https://fonts.googleapis.com/css2?family=Bebas+Neue&display=swap">
<style>
  :root {
    --sky-top: #2a76a8;
    --sky-mid: #4c9cc6;
    --sky-band: #8cc6de;
    --sky-floor: #c9e8f2;
    --title-white: #ffffff;
    --orb-light: #f4fbfd;
    --orb-mid: #9dd0e6;
    --orb-deep: #3c8fbc;
  }
  * { margin: 0; padding: 0; box-sizing: border-box; }
  html, body {
    width: 1200px;
    height: 1200px;
    overflow: hidden;
  }
  .cover {
    position: relative;
    width: 1200px;
    height: 1200px;
    overflow: hidden;
    background:
      radial-gradient(ellipse 900px 120px at 50% 58%, rgba(200,235,246,0.45), transparent 70%),
      linear-gradient(180deg,
        var(--sky-top) 0%,
        var(--sky-mid) 40%,
        var(--sky-band) 58%,
        var(--sky-mid) 66%,
        var(--sky-band) 82%,
        var(--sky-floor) 100%);
  }
  .cover-title {
    position: absolute;
    top: 78px;
    left: 0;
    width: 100%;
    text-align: center;
    color: var(--title-white);
    font-family: "Bebas Neue", "Oswald", sans-serif;
    font-weight: 400;
    line-height: 1;
    text-transform: uppercase;
    white-space: nowrap;
  }
  .cover-title .title-line {
    display: block;
    font-size: 186px;
    letter-spacing: 4px;
  }
  .cover-title .title-line--secondary {
    margin-top: 14px;
    letter-spacing: 8px;
  }
  .emblem-orb {
    position: absolute;
    left: 318px;
    top: 545px;
    width: 564px;
    height: 600px;
  }
</style>
</head>
<body>
  <main class="cover">
    <h1 class="cover-title">
      <span class="title-line title-line--primary">Mendral Access</span>
      <span class="title-line title-line--secondary">Roundtable</span>
    </h1>

    <svg class="emblem-orb" viewBox="0 0 564 600" role="img"
         aria-label="Glass sphere holding a golden caduceus medical emblem, resting on a soft blue surface">
      <defs>
        <radialGradient id="orbFill" cx="50%" cy="35%" r="65%">
          <stop offset="0%" stop-color="var(--orb-light)"/>
          <stop offset="45%" stop-color="var(--orb-mid)"/>
          <stop offset="100%" stop-color="var(--orb-deep)"/>
        </radialGradient>
        <radialGradient id="orbShadow" cx="50%" cy="50%" r="50%">
          <stop offset="0%" stop-color="#2a6f96" stop-opacity="0.35"/>
          <stop offset="100%" stop-color="#2a6f96" stop-opacity="0"/>
        </radialGradient>
      </defs>
      <ellipse cx="282" cy="540" rx="250" ry="34" fill="url(#orbShadow)"/>
      <circle cx="282" cy="282" r="262" fill="url(#orbFill)" opacity="0.92"/>
    </svg>
  </main>
</body>
</html>
```